Visitenkarten-Design für Integratives Business Coaching
Radoslava Tzvetkorina hat sehr zuverlässig, zügig und sorgfältig gearbeitet - herzlichen Dank!!
Zielgruppe
Ich bin Henrike Wendel | Vertriebs-Pfade L.U.X. Stärke® | Gründungs- und Unternehmensberatung (ZEFO-HWK)
Integratives Business Coaching für Start Ups, Unternehmer und alle, die eine berufliche Veränderung planen und ihre Selbständigkeit erfolgreich meistern wollen!
Aufgabenstellung
Das Design der VISITENKARTE sollte dem bestehenden Design meiner aktuellen Website https://henrike-wendel.com angepasst sein, ELEGANT aussehen und SERIÖS wirken:
Schriftart: Open sans
Schriftfarben: #0b2161 blau | #a8140f rot
Farbverlauf im Logo + auf der Website:
#a8130f
#edae44
Slogan: Business & Bewusstsein
Logo mit Schriftzug: siehe Upload
Profilbild: siehe Upload (das Photo muss noch gezoomt + zugeschnitten werden)

```html
<!DOCTYPE html>
<html lang="de">
<head>
<meta charset="utf-8">
<title>Visitenkarte Henrike Wendel</title>
<link href="https://fonts.googleapis.com/css2?family=Open+Sans:wght@400;600&display=swap" rel="stylesheet">
<style>
  :root {
    --stage: #3d3d3d;
    --card: #ffffff;
    --card-edge: #b9b9b9;
    --ink: #1a1a1a;
    --navy: #0b2161;
    --red: #a8140f;
    --grad-start: #a8130f;
    --grad-end: #edae44;
    --band: linear-gradient(90deg, #a8221a 0%, #c2521f 50%, #d9862a 100%);
    --bar: linear-gradient(90deg, #a8221a 0%, #b3321c 40%, #d9862a 100%);
    --photo: radial-gradient(circle at 45% 40%, #e8dccb 0%, #bfae98 45%, #5b5148 100%);
  }
  * { box-sizing: border-box; margin: 0; padding: 0; }
  html, body { width: 1095px; height: 1200px; overflow: hidden; }
  body {
    background: var(--stage);
    font-family: "Open Sans", Arial, sans-serif;
    position: relative;
  }
  .card {
    position: absolute;
    left: 124px;
    width: 820px;
    height: 475px;
    background: var(--card);
    border: 1px solid var(--card-edge);
    box-shadow: 0 2px 6px rgba(0,0,0,.35);
  }
  .card--front { top: 83px; }
  .card--back { top: 649px; }

  .brand {
    position: absolute;
    display: flex;
    align-items: center;
    color: var(--navy);
    font-weight: 400;
    white-space: nowrap;
  }
  .brand__dot { border-radius: 50%; background: var(--red); flex: none; }
  .brand--small { left: 61px; top: 48px; height: 61px; font-size: 19px; gap: 12px; }
  .brand--small .brand__dot { width: 61px; height: 61px; }
  .brand--large { left: 339px; top: 204px; height: 125px; font-size: 38px; gap: 24px; }
  .brand--large .brand__dot { width: 125px; height: 125px; }

  .portrait {
    position: absolute;
    left: 64px; top: 148px;
    width: 221px; height: 221px;
    border-radius: 50%;
    background: var(--photo);
  }

  .name-band {
    position: absolute;
    left: 341px;
    width: 440px; height: 76px;
    background: var(--band);
  }
  .card--front .name-band { top: 43px; }
  .card--back .name-band { top: 60px; }
  .name-band__text {
    color: #fff;
    font-size: 45px;
    font-weight: 400;
    line-height: 76px;
    padding-left: 12px;
    letter-spacing: 0.3px;
  }

  .tagline {
    position: absolute;
    left: 350px; top: 122px;
    color: var(--red);
    font-size: 19px;
    line-height: 26px;
  }
  .contact {
    position: absolute;
    left: 352px;
    color: var(--ink);
    font-size: 22px;
    line-height: 27.5px;
    font-style: normal;
  }
  .contact--address { top: 183px; }
  .contact--lines { top: 270px; }
  .rule {
    position: absolute;
    left: 346px;
    width: 440px; height: 12px;
    background: var(--bar);
  }
  .card--front .rule { top: 378px; }
  .card--back .rule { top: 395px; }
  .website {
    position: absolute;
    left: 356px; top: 412px;
    color: var(--ink);
    font-size: 22px;
    line-height: 30px;
  }
</style>
</head>
<body>
  <section class="card card--front">
    <div class="brand brand--small">
      <span class="brand__dot"></span>
      <span class="brand__name">Henrike Wendel</span>
    </div>
    <div class="portrait" role="img" aria-label="Porträtfoto von Henrike Wendel"></div>
    <div class="name-band"><h1 class="name-band__text">Henrike Wendel</h1></div>
    <p class="tagline">Vertriebs-Pfade L.U.X. Stärke</p>
    <address class="contact contact--address">Lindenhofweg 7b<br>80469 München</address>
    <p class="contact contact--lines">Tel: +49 89 41 72 30 58<br>Mobil: +49 152 337 90 612<br>willkommen@henrike-wendel.com</p>
    <div class="rule"></div>
    <p class="website">www.henrike-wendel.com</p>
  </section>

  <section class="card card--back">
    <div class="name-band"></div>
    <div class="brand brand--large">
      <span class="brand__dot"></span>
      <span class="brand__name">Henrike Wendel</span>
    </div>
    <div class="rule"></div>
  </section>
</body>
</html>
```